Bright Harbour Painting

Hi
I'm looking for a unique and eye-catching design for my business card that reflects the identity of my business. We specialize in residential, commercial, insurance, real state, heritage,and body corporate painting services and I want the card to make a memorable impression on potential clients.

Key elements to include are:
- Our logo (attached)
- Contact information: my name is dariush kamrani but my short name is dar, im a director of this business, number: 0458307715, email: info@brightharbourpainting.com.au
Website: www.brightharbourpainting.com.au
Social media: friendloop, snapgrid.

I'm open to creative ideas and unconventional formats, but it's important that the design maintains a professional look.

I'd like to see some initial concepts within the few days, and I'm willing to discuss any ideas you have.

Looking forward to seeing your creativity at work!

I prefer the colours pretty much the same as my logo, but i would be happy see if my logo match with other colours.
Thanks very much

Best regards,
Dar

Target Market(s)

Our target market consists of residential exterior and interior painting, basically we do all commercial jobs, bod corporate , heritage

Industry/Entity Type

Residential and commercial painting

Contact Information for Business Card

All my information as provided!! Im not sure if you guys have access to my logo through with all the format in my account??

Font styles to use
Serif

Requirements
Must have
• My business card should be double sided,
Nice to have
• Its nice to have all my information in front and the rest at the back, like what we we do like residential , interior exterior and as i mentioned

```html
<!DOCTYPE html>
<html lang="en">
<head>
<meta charset="utf-8">
<title>Bright Harbour Painting — Business Card</title>
<link href="https://fonts.googleapis.com/css2?family=Noto+Serif:wght@400;700&display=swap" rel="stylesheet">
<style>
  :root {
    --stage: #2b2b2d;
    --paper: #ffffff;
    --brand-blue: #0f64a8;
    --brand-blue-deep: #0b5391;
    --brand-red: #c0161f;
    --brand-green: #2e6a45;
    --ink: #2a2a2a;
  }
  * { margin: 0; padding: 0; box-sizing: border-box; }
  html, body { width: 1200px; height: 780px; overflow: hidden; }
  body {
    background: var(--stage);
    font-family: "Noto Serif", Georgia, serif;
    display: flex;
    flex-direction: column;
    align-items: center;
    justify-content: center;
    gap: 24px;
  }
  .card {
    width: 620px;
    height: 354px;
    position: relative;
    overflow: hidden;
  }

  /* Front side */
  .card--front { background: var(--paper); color: var(--ink); }
  .front__mark {
    position: absolute; left: 40px; top: 28px;
    width: 46px; height: 46px;
    border: 7px solid var(--brand-blue);
  }
  .front__edge-bar {
    position: absolute; left: 0; top: 108px;
    width: 14px; height: 46px;
    background: var(--brand-blue);
  }
  .person { position: absolute; left: 30px; top: 104px; }
  .person__name { font-size: 27px; font-weight: 700; line-height: 1.1; }
  .person__first { color: var(--brand-red); }
  .person__last { color: var(--brand-blue); }
  .person__role { font-size: 15px; margin-top: 2px; }
  .contacts {
    position: absolute; left: 30px; top: 186px;
    list-style: none; font-size: 14.5px; line-height: 1.55;
  }
  .contacts li { display: flex; align-items: center; gap: 8px; }
  .contacts svg { width: 13px; height: 13px; fill: var(--brand-blue); flex: none; }
  .front__brand {
    position: absolute; right: 38px; top: 150px;
    display: flex; align-items: center; gap: 12px;
    color: var(--brand-blue); font-weight: 700; font-size: 24px; line-height: 1.1;
    text-align: right;
  }
  .front__brand-square {
    width: 34px; height: 34px; border: 6px solid var(--brand-red); flex: none;
  }
  .social {
    position: absolute; right: 40px; bottom: 26px;
    display: flex; align-items: center; gap: 6px; font-size: 17px;
  }
  .social__dot { width: 20px; height: 20px; border-radius: 50%; background: var(--brand-blue); }
  .social__label { margin-left: 8px; }

  /* Back side */
  .card--back {
    background: var(--brand-blue);
    display: flex; align-items: center; justify-content: center; gap: 20px;
  }
  .back__square {
    width: 70px; height: 70px; border: 10px solid var(--brand-blue-deep);
  }
  .back__brand {
    color: var(--brand-blue-deep); font-weight: 700; font-size: 38px; line-height: 1.1;
  }
</style>
</head>
<body>
  <section class="card card--front" aria-label="Business card front">
    <div class="front__mark"></div>
    <div class="front__edge-bar"></div>
    <div class="person">
      <p class="person__name"><span class="person__first">Dariush</span> <span class="person__last">Kamrani</span></p>
      <p class="person__role">Director</p>
    </div>
    <ul class="contacts">
      <li>
        <svg viewBox="0 0 16 16" aria-hidden="true"><path d="M3.6 1.2l2.3 2.3-1.3 2a9 9 0 005.9 5.9l2-1.3 2.3 2.3-1.4 2.4C7 14.6 1.4 9 .8 2.6z"/></svg>
        0458307715
      </li>
      <li>
        <svg viewBox="0 0 16 16" aria-hidden="true"><path d="M1 3h14v10H1zm1.5 1.5v.3L8 8.7l5.5-3.9v-.3zm0 2.2v4.8h11V6.7L8 10.6z"/></svg>
        info@brightharbourpainting.com.au
      </li>
      <li>
        <svg viewBox="0 0 16 16" aria-hidden="true"><path d="M8 1a7 7 0 100 14A7 7 0 008 1zm0 1.6c.9 1 1.5 2.4 1.7 4.4H6.3C6.5 5 7.1 3.6 8 2.6zM2.7 9h2.6c.1 1.6.5 3 1.1 4a5.4 5.4 0 01-3.7-4zm0-2a5.4 5.4 0 013.7-4c-.6 1-1 2.4-1.1 4zm5.3 6.4c-.9-1-1.5-2.4-1.7-4.4h3.4c-.2 2-.8 3.4-1.7 4.4zm1.6-.4c.6-1 1-2.4 1.1-4h2.6a5.4 5.4 0 01-3.7 4zm1.1-6c-.1-1.6-.5-3-1.1-4a5.4 5.4 0 013.7 4z"/></svg>
        www.brightharbourpainting.com.au
      </li>
    </ul>
    <div class="front__brand">
      <span class="front__brand-square"></span>
      <span>Bright Harbour<br>Painting</span>
    </div>
    <div class="social">
      <span class="social__dot"></span>
      <span class="social__dot"></span>
      <span class="social__label">friendloop, snapgrid</span>
    </div>
  </section>

  <section class="card card--back" aria-label="Business card back">
    <span class="back__square"></span>
    <span class="back__brand">Bright Harbour<br>Painting</span>
  </section>
</body>
</html>
```